WHAT LIES BEYOND? Discovering the shape of days with the Silent Lamp

Creating a book that is about living a spiritual life. The book is about letting go of the materialistic world and finding happiness through self realisation and enlightenment. The contents page is below that gives an idea of what is contained in the book.

The book is based on the writings of the Sikhs - from India. But it is written in a universal way that is understandable to all.

CONTENTS
Living for a purpose
- Born to be original! Dying as a copy!
- My relationship with everything but me!
- What is my purpose?

Life as a human being!
- Stages of Life
- Five Weaknesses

What is driving our lives?
- Information overload?
- What are your drivers?
- Giving life meaning

You reap what you sow
- Is my destiny written?
- Good and bad actions
- Maya – the illusion and it’s three modes

Slow down and let go
- The mind in overdrive
- Being aware of our mental health
- Why Slow Down?

The Guidance of the Guru
- Why do I need a Guru?
- What the Guru gives you
- Gurbani – the Guru’s Words

Staying connected
- Repeating the Mantra
- Doing two things at once
- Remembering in times of difficulty

Cultivating virtues
- Theory vs Practice
- Virtues and true religion
- Some key virtues

The Mystical Creation
- Experiencing ecstasy
- Enlightenment and intuition
- Spiritual Transformation

Good Company
- How do my companions affect me?
- The company of Saintly people
- Obtaining the fruits that the Guru describes

Serving selflessly
- Serving is our purpose
- Being grateful
- Being generous

Ten things to change your life today

Target Market(s)

All those who want to learn about spirituality. We are targeting young and middle aged but not necessarily ruling out older demographic.

Requirements
Must have
• The book cover:

- exciting and intriguing
- theme is "what lies beyond" in this world
- some kind of lean towards enlightenment
Nice to have
• It is not essential but the cover could subtly show something about the Sikh faith. Can discuss this further if necessary.
Should not have
• Should not:

- look dull and boring
- don't want it to look like a Buddhism book

```html
<!DOCTYPE html>
<html lang="en">
<head>
<meta charset="utf-8">
<title>What Lies Beyond – Book Cover</title>
<link rel="stylesheet" href="https://fonts.googleapis.com/css2?family=Playfair+Display:wght@700;800&display=swap">
<style>
  :root {
    --backdrop: #dcddd8;
    --cover-ochre: #c9b45a;
    --cover-amber: #e9b457;
    --cover-cream: #f4eccf;
    --cover-mint: #dfe9d6;
    --art-red: #c2432c;
    --art-plum: #7c3f52;
    --title-deep: #7e1a28;
    --title-bright: #e0303f;
    --tagline: #4a1712;
  }
  * { margin: 0; padding: 0; box-sizing: border-box; }
  html, body {
    width: 1200px;
    height: 853px;
    overflow: hidden;
    background: var(--backdrop);
  }
  .canvas {
    position: relative;
    width: 1200px;
    height: 853px;
  }
  .cover {
    position: absolute;
    left: 324px;
    top: 26px;
    width: 552px;
    height: 800px;
    overflow: hidden;
    background:
      linear-gradient(100deg, var(--cover-ochre) 0%, var(--cover-amber) 30%, var(--cover-cream) 65%, var(--cover-mint) 100%);
    font-family: "Playfair Display", Georgia, serif;
  }
  .cover-art {
    position: absolute;
    left: 0;
    top: 0;
    width: 552px;
    height: 600px;
    background:
      radial-gradient(ellipse 190px 170px at 215px 250px, rgba(194,67,44,0.85), rgba(194,67,44,0) 100%),
      radial-gradient(ellipse 150px 130px at 320px 300px, rgba(124,63,82,0.55), rgba(124,63,82,0) 100%),
      radial-gradient(ellipse 170px 120px at 250px 470px, rgba(250,246,230,0.9), rgba(250,246,230,0) 100%),
      linear-gradient(180deg, rgba(246,236,205,0.9) 0%, rgba(246,236,205,0) 16%, rgba(255,255,255,0) 100%);
  }
  .tagline {
    position: absolute;
    top: 13px;
    left: 0;
    width: 552px;
    text-align: center;
    font-size: 12px;
    line-height: 1;
    font-weight: 700;
    letter-spacing: 0.04em;
    color: var(--tagline);
  }
  .title {
    position: absolute;
    left: 0;
    top: 0;
    width: 552px;
    height: 800px;
  }
  .title-main,
  .title-sub,
  .title-tail {
    position: absolute;
    display: block;
    white-space: nowrap;
    line-height: 1;
  }
  .title-main,
  .title-sub {
    background: linear-gradient(90deg, var(--title-deep) 0%, var(--title-bright) 100%);
    -webkit-background-clip: text;
    background-clip: text;
    color: transparent;
  }
  .title-main {
    left: 58px;
    top: 483px;
    font-size: 188px;
    font-weight: 800;
    letter-spacing: -0.02em;
  }
  .title-sub {
    left: 80px;
    top: 689px;
    font-size: 47px;
    font-weight: 700;
  }
  .title-tail {
    left: 92px;
    top: 754px;
    font-size: 20px;
    font-weight: 700;
    color: var(--title-deep);
  }
</style>
</head>
<body>
  <main class="canvas">
    <section class="cover">
      <div class="cover-art" role="img" aria-label="Cover artwork area in warm red, amber and cream painted tones"></div>
      <p class="tagline">EXCITING AND INTRIGUING</p>
      <h1 class="title">
        <span class="title-main">What</span>
        <span class="title-sub">LIES BEYOND</span>
        <span class="title-tail">IN THIS WORLD</span>
      </h1>
    </section>
  </main>
</body>
</html>
```